Geschäftspapiere Campingplatz
Zielgruppe
Campingplatz
Aufgabenstellung
Geschäftspapiere, Briefpapier, Visitenkarte, Briefumschlag und DIN A5 Memoblock farblich und designmäßig am Logo orientiert.
Memoblock sollte sich vom Briefpapier unterscheiden und nicht so viele Daten enthalten.
Website, E-Mail, Telefonnummer, Festnetz, Adresse und Inhaber sollen auf dem Briefpapier erscheinen.
Auf der Visitenkarte soll nur statt Inhaber stehen und zusätzlich die Handynummer, sowie alle anderen Daten.
Die Datensätze sollten sich mit entsprechendem Programm von uns bearbeiten lassen.

```html
<!DOCTYPE html>
<html lang="de">
<head>
<meta charset="utf-8">
<title>Camping Talwiese – Geschäftspapiere</title>
<link rel="stylesheet" href="https://fonts.googleapis.com/css2?family=Source+Sans+3:wght@400;600;700&display=swap">
<style>
  :root{
    --bg:#f7f7f7;
    --paper:#ffffff;
    --olive:#b09a2e;
    --green:#6e9628;
    --orange:#e87a2a;
    --ink:#333333;
    --grey:#666666;
    --envelope:#f1f1f1;
    --window:#e4e4e4;
  }
  *{margin:0;padding:0;box-sizing:border-box}
  html,body{width:1200px;height:1000px;overflow:hidden;background:var(--bg)}
  body{position:relative;font-family:"Source Sans 3",Arial,sans-serif;color:var(--ink)}
  .abs{position:absolute}
  .brand{font-weight:700;color:var(--green);white-space:nowrap;letter-spacing:.01em}
  .label{color:var(--orange)}

  /* Hero wordmark */
  .hero-mark{left:85px;top:60px;width:435px;height:130px;display:flex;align-items:center;justify-content:center;gap:14px}
  .hero-mark .brand{font-size:62px}
  .hero-mark .dot{width:26px;height:26px;border-radius:50%;background:var(--olive);flex:none}

  /* Letterhead */
  .letterhead{left:36px;top:213px;width:533px;height:753px;background:var(--paper);box-shadow:1px 1px 4px rgba(0,0,0,.25)}
  .letterhead .band-gold{left:0;top:0;width:9px;height:124px;background:var(--olive)}
  .letterhead .band-green{left:0;top:133px;width:9px;height:620px;background:var(--green)}
  .letterhead .fold{left:9px;width:16px;height:1px;background:#555}
  .letterhead .mark{left:322px;top:48px;width:181px;text-align:center}
  .letterhead .mark .brand{font-size:24px}
  .letterhead .sender{left:67px;top:136px;display:flex;align-items:center;gap:7px;font-size:6px;color:var(--grey)}
  .letterhead .sender .dot{width:16px;height:16px;border-radius:50%;border:2px solid var(--green)}
  .letterhead .contact{left:379px;top:113px;padding-left:4px;border-left:1px solid var(--olive);font-size:8px;width:150px}
  .contact .brand{font-size:10px;line-height:14px}
  .contact p{line-height:11px}
  .contact .gap{margin-top:11px}
  .contact .gap-s{margin-top:4px}
  .contact .pad{display:inline-block;width:31px}
  .letterhead .footer{top:717px;font-size:7.5px;line-height:8.5px;color:var(--grey)}
  .letterhead .divider{top:715px;width:1px;height:23px;background:#555}

  /* Business cards */
  .card{width:345px;height:225px;background:var(--paper);box-shadow:3px 3px 5px rgba(0,0,0,.55)}
  .card-front{left:696px;top:40px}
  .card-back{left:702px;top:297px}
  .card-front .holder{left:32px;top:40px;font-size:14px;color:var(--grey)}
  .card-front .bar-top{left:123px;top:45px;width:222px;height:9px;background:var(--olive)}
  .card-front .bar-bottom{left:0;top:191px;width:196px;height:9px;background:var(--olive)}
  .card-front .address{left:56px;top:120px;font-size:7.5px;line-height:10px}
  .card-front .contact{left:207px;top:107px;font-size:7.5px;width:135px}
  .card-front .contact .brand{font-size:10px;line-height:14px}
  .card-front .contact p{line-height:12.7px}
  .card-back .mark{left:0;top:0;width:345px;height:225px;display:flex;align-items:center;justify-content:center}
  .card-back .mark .brand{font-size:28px}

  /* Envelope */
  .envelope{left:633px;top:537px;width:498px;height:429px}
  .envelope svg{position:absolute;left:0;top:0;filter:drop-shadow(3px 3px 3px rgba(0,0,0,.45))}
  .envelope .format{left:358px;top:92px;font-size:36px;color:#555;font-weight:400}
  .envelope .window{left:45px;top:158px;width:195px;height:76px;border-radius:10px;background:var(--window)}
  .envelope .rule{left:0;top:371px;width:317px;height:1px;background:#777}
  .envelope .mark{left:334px;top:360px;width:137px;text-align:center}
  .envelope .mark .brand{font-size:17px}
  .envelope .return{left:44px;top:386px;width:100px;text-align:center;font-size:9px;line-height:12px}
</style>
</head>
<body>

  <div class="abs hero-mark">
    <span class="dot"></span>
    <span class="brand">Camping Talwiese</span>
  </div>

  <section class="abs letterhead" aria-label="Briefpapier">
    <div class="abs band-gold"></div>
    <div class="abs band-green"></div>
    <div class="abs fold" style="top:265px"></div>
    <div class="abs fold" style="top:518px"></div>

    <div class="abs mark"><span class="brand">Camping Talwiese</span></div>

    <div class="abs sender">
      <span class="dot"></span>
      <span>Lindenweg 12&nbsp;&nbsp;&nbsp;&nbsp;71234 Musterau am Fluss</span>
    </div>

    <div class="abs contact">
      <div class="brand">Camping Talwiese</div>
      <p>Marlene Reiter</p>
      <p class="gap" style="margin-top:17px">Address here, number</p>
      <p>City, Country</p>
      <p class="gap-s" style="margin-top:5px"><span class="label pad">Telefon:</span>55 555-555-555</p>
      <p><span class="label">Mobile:</span></p>
      <p>Marlene 55 555-555-555</p>
      <p>Tobias 55 555-555-555</p>
      <p class="gap-s" style="margin-top:2px"><span class="label pad">E-mail:</span>email@yourdomain.com</p>
      <p style="margin-top:1px"><span class="label pad">Web:</span>www.yourwebsite.com</p>
    </div>

    <div class="abs footer" style="left:79px">Bankverbindung<br>Talbank Mittelland eG<br>Konto 000000000r</div>
    <div class="abs divider" style="left:215px"></div>
    <div class="abs footer" style="left:238px">BLZ: 0000y760000<br>Steurnummer: 000/870000<br>Ust-ID: DE 00008900000</div>
    <div class="abs divider" style="left:357px"></div>
    <div class="abs footer" style="left:381px;top:720px">BIC: ETFUuhYGYGU<br>IBAN: 700007900000</div>
  </section>

  <section class="abs card card-front" aria-label="Visitenkarte Vorderseite">
    <div class="abs holder">Fam Reiter</div>
    <div class="abs bar-top"></div>
    <div class="abs address">Address here, number<br>City, Country</div>
    <div class="abs contact">
      <div class="brand">Camping Talwiese</div>
      <p><span class="label">Telefon:</span>&nbsp; 55 555-555-555</p>
      <p><span class="label">Mobile:</span></p>
      <p>Marlene 55 555-555-555</p>
      <p>Tobias 55 555-555-555</p>
      <p><span class="label">E-mail:</span>&nbsp;&nbsp; email@yourdomain.com</p>
      <p style="margin-top:3px"><span class="label">Web:</span>&nbsp; www.yourwebsite.com</p>
    </div>
    <div class="abs bar-bottom"></div>
  </section>

  <section class="abs card card-back" aria-label="Visitenkarte Rückseite">
    <div class="abs mark"><span class="brand">Camping Talwiese</span></div>
  </section>

  <section class="abs envelope" aria-label="Briefumschlag">
    <svg width="498" height="429" viewBox="0 0 498 429">
      <path d="M0 76 L25 20 Q34 0 56 0 L448 0 Q470 0 478 20 L498 76 L498 429 L0 429 Z" fill="var(--envelope)"/>
      <line x1="0" y1="76" x2="498" y2="76" stroke="#777" stroke-width="0.8"/>
    </svg>
    <div class="abs format">Din A5</div>
    <div class="abs window"></div>
    <div class="abs rule"></div>
    <div class="abs mark"><span class="brand">Camping Talwiese</span></div>
    <div class="abs return">Address here, number<br>City, Country</div>
  </section>

</body>
</html>
```